Web re-design project www.vempresoft.com

We need a corporate website for a startup company called Vempre Labs. The company offers web-based worksite management system for big construction companies. In short, replacing annoying papers with iPads.
We need the site main page to provide basic overview of the company and then inner page layout for displaying news and detailed information about products.
Currently we have a site up at:
http://www.vempresoft.com/en/main
but as you can see the graphic design is a bit lacking in quality(implemented by a tech guy :)
We need you to pimp that web site design up!
There is possibility for more freelance work in the future related to our web products, slide show designs and printed marketing materials.
Our main product is LOMVI. You can find a short presentation about what it does here:
http://www.vempresoft.com/en/lomvi
Here you can find packages of images and screenshots related to our company:
https://files.plimbox.net/u/7719026/vempre_images.zip
https://files.plimbox.net/u/7719026/vempresoft%20images2.zip
Product logo svg can be found here:
https://files.plimbox.net/u/7719026/LOMVI-logo.svg
Your are not forced to use those images, but hopefully there will be something that is useful.
Hope to hear from you guys soon!
Cheers,
Ossi
Update:
We will be using LOMVI logo as the company brand. I don't like our current Vempre Labs company logo, so that doesn't need to be included in the site design.
Update 2:
I like website designs that are "light", elegant and pretty simplistic. One example is our product login page (screenshot included in files).
Update 3:
Sites from the same industry / type of products:
http://www.rakmoda.fi/
http://www.quarvelgrid.com/products/software/network-applications/fieldsync-3d
http://www.dornvex.com/construction/heavy-civil/software-solutions/Linked-Network.aspx?dtID=overview&
Target audience for the website is companies in the construction sector, and possibly corporate investors
Graphic Design

```html
<!DOCTYPE html>
<html lang="en">
<head>
<meta charset="utf-8">
<title>Vempre Labs</title>
<link rel="stylesheet" href="https://fonts.googleapis.com/css2?family=Oswald:wght@300;400&family=Source+Sans+3:wght@400;600&display=swap">
<style>
:root{
  --ink:#1a1a1a;
  --text:#2b2b2b;
  --muted:#555;
  --line:#d9d9d9;
  --frame:#e3e3e3;
  --panel:#e6e6e6;
  --orange:#f28a1c;
  --orange-dark:#e56a0a;
  --nav:#0e0e0e;
  --footer:#f2f2f2;
}
*{margin:0;padding:0;box-sizing:border-box}
html,body{width:1200px;height:1015px;overflow:hidden;background:#fff}
body{position:relative;font-family:"Source Sans 3",Arial,sans-serif;color:var(--text)}
.abs{position:absolute}
.brand{left:152px;top:10px;font-family:"Source Sans 3",sans-serif;font-size:30px;font-weight:400;color:var(--ink);letter-spacing:-.5px}
.lang{left:949px;top:4px;font-size:11px;color:#444;display:flex;gap:7px}
.lang span+span{border-left:1px solid #bbb;padding-left:7px}
.search{left:822px;top:27px;width:147px;height:27px;border-radius:6px;background:linear-gradient(#f4f4f4,#fff);border:1px solid #d4d4d4;box-shadow:0 2px 3px rgba(0,0,0,.15)}
.search svg{position:absolute;left:11px;top:6px}
.btn{background:linear-gradient(#f9a24a,var(--orange-dark));color:#fff;border-radius:4px;text-align:center;box-shadow:0 1px 3px rgba(0,0,0,.25)}
.search-btn{left:977px;top:27px;width:62px;height:25px;font-size:12px;line-height:25px}
.nav{left:157px;top:66px;width:885px;height:28px;background:linear-gradient(#2a2a2a,var(--nav));border-radius:3px;display:flex}
.nav a{color:#fff;text-decoration:none;font-size:11px;line-height:28px;text-align:center;border-right:1px solid #555}
.nav a:last-child{border-right:0}
.slider{left:157px;top:102px;width:884px;height:383px;background:var(--frame);border-radius:10px;box-shadow:0 18px 16px -10px rgba(0,0,0,.35)}
.hero{left:7px;top:7px;width:870px;height:369px;background:linear-gradient(110deg,#b7bfb6 0%,#8f8a7f 35%,#9b8377 60%,#8a7469 100%)}
.caption{left:437px;top:71px;width:433px;height:148px;background:rgba(120,100,90,.45)}
.caption p{position:absolute;left:24px;top:16px;font-family:Oswald,sans-serif;font-weight:300;font-size:26px;line-height:37px;color:#fff;text-transform:uppercase;letter-spacing:-.3px}
.arrow{width:66px;height:66px;border-radius:50%;background:#e6e6e6;top:159px}
.arrow svg{position:absolute;top:21px}
.arrow.prev{left:-26px}.arrow.prev svg{left:32px}
.arrow.next{left:844px}.arrow.next svg{left:22px}
.card{top:533px;width:222px}
.card .thumb{height:101px;border:1px solid #bbb;border-radius:3px}
.card h3{font-family:Oswald,sans-serif;font-weight:400;font-size:17px;margin-top:11px;text-transform:uppercase;color:var(--ink)}
.card p{font-size:11.5px;line-height:15px;margin-top:2px;color:var(--ink)}
.card .rule{position:absolute;top:190px;left:0;width:221px;border-top:1px solid var(--line)}
.newsletter{left:163px;top:740px;width:687px;height:88px;background:var(--panel);border-radius:3px}
.newsletter .label{position:absolute;left:47px;top:30px;font-family:Oswald,sans-serif;font-size:17px;text-transform:uppercase;color:var(--ink)}
.newsletter .input{position:absolute;left:197px;top:29px;width:322px;height:29px;background:#fff;border:1px solid #d2d2d2;border-radius:3px;font-size:11px;line-height:27px;padding-left:10px}
.newsletter .btn{position:absolute;left:528px;top:29px;width:103px;height:28px;font-family:Oswald,sans-serif;font-weight:300;font-size:15px;line-height:28px}
.news{left:865px;top:531px;width:176px;height:298px;background:var(--frame);border-radius:8px}
.news .inner{position:absolute;left:7px;top:7px;right:7px;bottom:7px;background:#fff;border-radius:3px;padding:7px 8px 0 9px}
.news h2{font-family:Oswald,sans-serif;font-weight:400;font-size:17px;text-transform:uppercase;color:var(--ink);padding-bottom:6px;border-bottom:1px solid var(--line)}
.item{padding:11px 0 6px 8px;font-size:11.5px;line-height:16.5px;text-align:justify}
.item .date{display:flex;align-items:center;gap:9px;margin-bottom:8px;text-align:left}
.item+.item{border-top:1px solid var(--line);padding-top:10px}
.footer{left:0;top:846px;width:1200px;height:169px;background:linear-gradient(#f0f0f0,#fff 60%);border-top:1px solid #e2e2e2}
.follow{top:868px;width:1200px;text-align:center;font-size:12px;color:var(--ink)}
.social{left:550px;top:894px;display:flex;gap:5px}
.social span{width:22px;height:22px;border-radius:3px}
.f-rule{left:163px;width:874px;border-top:1px solid #ddd}
.f-links{top:943px;width:1200px;text-align:center;font-size:11px;color:var(--ink)}
.f-links i{font-style:normal;margin:0 6px}
.copy{top:980px;width:1200px;text-align:center;font-size:11px;color:var(--ink)}
</style>
</head>
<body>
<div class="abs brand">Vempre Labs</div>
<div class="abs lang"><span>ENGLISH</span><span>FINNISH</span></div>
<div class="abs search"><svg width="14" height="14" viewBox="0 0 14 14"><circle cx="5.5" cy="5.5" r="4" fill="none" stroke="#888" stroke-width="1.6"/><line x1="8.5" y1="8.5" x2="13" y2="13" stroke="#777" stroke-width="2"/></svg></div>
<div class="abs btn search-btn">SEARCH</div>

<nav class="abs nav">
  <a style="width:129px">HOME</a><a style="width:144px">ABOUT US</a><a style="width:146px">PRODUCTS</a><a style="width:158px">UPCOMMING PROJECTS</a><a style="width:146px">NEWS</a><a style="width:162px">CONTACT US</a>
</nav>

<section class="abs slider">
  <div class="abs hero" role="img" aria-label="Site engineer in hard hat using a tablet on a road construction site with an excavator behind"></div>
  <div class="abs caption" style="left:444px;top:78px"><p>LOMVI is a cloud-based service for<br>road construction projects and it's<br>going full steam!</p></div>
  <div class="abs arrow prev"><svg width="14" height="24" viewBox="0 0 14 24"><path d="M12 2 3 12l9 10" fill="none" stroke="#222" stroke-width="3"/></svg></div>
  <div class="abs arrow next"><svg width="14" height="24" viewBox="0 0 14 24"><path d="M2 2l9 10-9 10" fill="none" stroke="var(--orange-dark)" stroke-width="3"/></svg></div>
</section>

<article class="abs card" style="left:160px">
  <div class="thumb" role="img" aria-label="Workers beside a yellow excavator in a green field" style="background:linear-gradient(120deg,#6f8a4e,#c9a23a 45%,#5a7440)"></div>
  <h3>About Us</h3>
  <p>LOMVI is a cloud-based service for road construction projects and it's going full steam!</p>
  <div class="rule"></div>
</article>
<article class="abs card" style="left:394px">
  <div class="thumb" role="img" aria-label="Hand holding a tablet showing a site plan over paper drawings" style="background:linear-gradient(120deg,#d9d4c8,#4a4a48 45%,#e4e0d8)"></div>
  <h3>Projects</h3>
  <p>LOMVI is a cloud-based service for road construction projects and it's going full steam!</p>
  <div class="rule"></div>
</article>
<article class="abs card" style="left:628px">
  <div class="thumb" role="img" aria-label="Illustration of an office worker at a computer linked to a map of worksite machines" style="background:linear-gradient(120deg,#efefef,#e8dfc6 60%,#d8d1b8)"></div>
  <h3>Products</h3>
  <p>LOMVI - WEB based Worksite Data Manage-<br>ment service</p>
  <div class="rule"></div>
</article>

<section class="abs newsletter">
  <div class="label">Newsletter Signup <svg width="8" height="12" viewBox="0 0 8 12" style="margin-left:4px"><path d="M0 0l8 6-8 6z" fill="#333"/></svg></div>
  <div class="input">Enter your E mail id</div>
  <div class="btn">SIGN UP</div>
</section>

<aside class="abs news">
  <div class="inner">
    <h2>News</h2>
    <div class="item">
      <div class="date"><svg width="14" height="14" viewBox="0 0 14 14"><circle cx="7" cy="7" r="6" fill="#eee" stroke="#aaa"/><path d="M5.5 4.5 9 7l-3.5 2.5z" fill="#555"/></svg>25.10.2012</div>
      Vempre Labs new website has been launched. From these pages you can find information about LOMVI cloud-based road con-struction service and other products from Vempre Labs.
    </div>
    <div class="item">
      <div class="date"><svg width="14" height="14" viewBox="0 0 14 14"><circle cx="7" cy="7" r="6" fill="#eee" stroke="#aaa"/><path d="M5.5 4.5 9 7l-3.5 2.5z" fill="#555"/></svg>24.10.2012</div>
      Vempre Labs new website has been launched. From these pages...
    </div>
  </div>
</aside>

<footer>
  <div class="abs footer"></div>
  <div class="abs follow">Follow us on</div>
  <div class="abs social" aria-label="Social links">
    <span style="background:#3b5a9a"></span><span style="background:#3fa9e0"></span><span style="background:#1b6fa8"></span><span style="background:#f28a1c"></span>
  </div>
  <div class="abs f-rule" style="top:931px"></div>
  <div class="abs f-links">Home<i>\</i>About Us<i>\</i>Products<i>\</i>Upcomming Projects<i>\</i>News<i>\</i>Contact us</div>
  <div class="abs f-rule" style="top:967px"></div>
  <div class="abs copy">Copyrights @ 2012 All Rights Reserved</div>
</footer>
</body>
</html>
```